PLM Business Card Design

Services for small businesses: Bookkeeping
BAS
Payroll
Software advice and sales
Can provide training for staff
Programs used: MYOB, Reckon, Xero
Clients software or mine.
Inhouse or external (pickup paperwork, process and return)
I provide individual solutions based on the clients business
I am a sole trader
Industry/Entity Type
Training
Contact Information for Business Card
PLM Bookkeeping Solutions
Marianne Tollbury, Qualified Bookkeeping Consultant
Registered BAS Agent
PO Box 862, Brookvale Park SA 5209
P: 0491 576 318
F: 08 8675 9041
Logo Text
PLM Bookkeeping Solutions
Requirements
Must have
- I don't have a logo but anything financial would be great.
My name, title, business name, Registered BAS agent, contact details.
Nice to have
- The "nice to haves" are the types of services (ie: Payroll, Bookkeeping, etc) and the software to be used (ie: MYOB, Reckon, Xero).

```html
<!DOCTYPE html>
<html lang="en">
<head>
<meta charset="utf-8">
<title>PLM Bookkeeping Solutions – Business Card</title>
<link rel="stylesheet" href="https://fonts.googleapis.com/css2?family=Pinyon+Script&family=Crimson+Pro:wght@400;700&display=swap">
<style>
  :root {
    --page-bg: #ece8e2;
    --card-white: #ffffff;
    --ink: #1a1a1a;
    --accent-red: #e0262b;
    --photo-light: #e6e6e6;
    --photo-mid: #9a9a9a;
    --photo-dark: #2e2e2e;
  }
  html, body {
    margin: 0;
    padding: 0;
    width: 1200px;
    height: 1000px;
    overflow: hidden;
    background: var(--page-bg);
  }
  .canvas {
    width: 1200px;
    height: 1000px;
    display: flex;
    flex-direction: column;
    align-items: center;
    justify-content: center;
    gap: 40px;
  }
  .card {
    position: relative;
    width: 770px;
    height: 440px;
    background: var(--card-white);
    overflow: hidden;
    box-shadow: 0 2px 10px rgba(0,0,0,0.15);
  }

  /* Wordmark: invented name, one colour, one weight */
  .wordmark {
    display: flex;
    align-items: center;
    gap: 10px;
    font-family: "Crimson Pro", serif;
    font-weight: 400;
    font-size: 24px;
    line-height: 1;
    color: var(--ink);
    white-space: nowrap;
  }
  .wordmark__square {
    width: 14px;
    height: 14px;
    background: var(--ink);
    flex: none;
  }

  /* Front */
  .card--front .wordmark { position: absolute; top: 32px; right: 36px; }
  .holder {
    position: absolute;
    left: 48px;
    top: 92px;
    font-family: "Crimson Pro", serif;
    color: var(--ink);
  }
  .holder__name {
    font-family: "Pinyon Script", cursive;
    font-size: 56px;
    line-height: 1.1;
    margin: 0 0 4px;
    font-weight: 400;
  }
  .holder__title { font-weight: 700; font-size: 23px; line-height: 1.3; margin: 0 0 2px; }
  .holder__line { font-size: 20px; line-height: 1.35; margin: 0; }
  .card--front .photo {
    position: absolute;
    left: 0;
    top: 300px;
    width: 700px;
    height: 112px;
    background: linear-gradient(100deg, var(--photo-light) 0%, #cfcfcf 35%, var(--photo-mid) 65%, var(--photo-dark) 100%);
  }
  .accent-bar {
    position: absolute;
    left: 712px;
    top: 262px;
    width: 34px;
    height: 150px;
    background: var(--accent-red);
  }

  /* Back */
  .card--back .photo {
    position: absolute;
    inset: 0;
    background: linear-gradient(135deg, var(--photo-dark) 0%, var(--photo-mid) 25%, var(--photo-light) 50%, #cfcfcf 70%, var(--photo-dark) 100%);
  }
  .card--back .wordmark {
    position: absolute;
    left: 290px;
    top: 170px;
  }
</style>
</head>
<body>
<main class="canvas">
  <section class="card card--front">
    <div class="wordmark">
      <span class="wordmark__square"></span>
      <span class="wordmark__name">PLM Bookkeeping Solutions</span>
    </div>
    <div class="holder">
      <h1 class="holder__name">Marianne Tollbury</h1>
      <p class="holder__title">Qualified Bookkeeping Consultant</p>
      <p class="holder__line">Registered BAS Agent PO Box 862</p>
      <p class="holder__line">Brookvale Park SA 5209</p>
      <p class="holder__line">P: 0491 576 318 | F: 08 8675 9041</p>
    </div>
    <div class="photo" role="img" aria-label="Photo of a desk with a stamp, a silver pen and a calculator resting on printed tax statements"></div>
    <div class="accent-bar"></div>
  </section>

  <section class="card card--back">
    <div class="photo" role="img" aria-label="Close-up photo of a stamp, silver pen, calculator and phone on printed financial statements"></div>
    <div class="wordmark">
      <span class="wordmark__square"></span>
      <span class="wordmark__name">PLM Bookkeeping Solutions</span>
    </div>
  </section>
</main>
</body>
</html>
```